Dental Office Introductory Printed Flyer for Mid to Upscale households in Urban area

Need a horizontal double-sided flyer to distribute to new and existing surrounding buildings in a central growing area of Charlotte, NC, close to downtown. We are a new dental practice, and want to promote our service with an introductory offer that includes free Veltora Brightwave toothbrush or an in-office bleaching.
Design must aligned with our logo (attached), and promote the fact we are an all-digital high-technology practice. We do same-day LUMAX crowns, cosmetic veneers, whitening, tooth-colored compositve (fillings), Clear orhtodontic treatments (alignira), root canals, LUMAX onlay/inlays,

Target Market(s)

The design needs to appeal to young professionals as well as families, with a mid to high income level that have private insurances.

Industry/Entity Type

Dental Clinic

Font styles to use
Sans Serif

Colors
0555a3
f37122

Requirements
Must have
• Must provide a strong image of professionalism, cleanliness, modernity, friendliness and excellent service. Convey a vibrant atmosphere and energy.
• Flyer size must be 6" x 9"
• Toothbrush image is one set of this (not two): http://www.mirovend.com/wp-content/uploads/2015/06/Veltora-Brightwave-QM4817-32-Glidefresh-Electric-Toothbrush1.jpg
• Mention we have flexible payment options with PayBloom, and that we work with most insurance plans
Nice to have
• Ideally it should include picture of the Dentist and some of the services in our website - www.brenwickdentalhub.com

```html
<!DOCTYPE html>
<html lang="en">
<head>
<meta charset="utf-8">
<title>Brenwick DentalHub – Introductory Flyer</title>
<link rel="stylesheet" href="https://fonts.googleapis.com/css2?family=Arimo:wght@400;700&family=Oswald:wght@600&family=Lato:wght@400&family=Cormorant+Garamond:ital,wght@1,500;1,600&display=swap">
<style>
:root{
  --blue:#0555a3;
  --orange:#f37122;
  --orange-light:#fbc9a6;
  --ink:#2b2b2b;
  --grey:#595959;
  --paper:#ffffff;
  --backdrop:#ececec;
  --stamp:#a7a7a9;
}
*{box-sizing:border-box;margin:0;padding:0}
html,body{width:832px;height:1200px;overflow:hidden}
body{background:var(--backdrop);position:relative;font-family:"Lato",sans-serif}
.card{position:absolute;left:44px;width:744px;height:496px;background:var(--paper);overflow:hidden}
.card--front{top:83px}
.card--back{top:612px}
.card__shapes{position:absolute;inset:0;width:744px;height:496px}
.brand{position:absolute;display:flex;align-items:flex-start;gap:8px}
.brand__mark{width:22px;height:22px;background:var(--orange);margin-top:6px}
.brand__name{font-family:"Arimo",sans-serif;font-weight:400;color:var(--blue);font-size:27px;line-height:25px}
.brand__tagline{font-family:"Arimo",sans-serif;font-size:7.5px;color:var(--blue);margin-top:5px;border-top:1px solid var(--blue);padding-top:2px;white-space:nowrap}
.card--front .brand{left:46px;top:22px}
.card--back .brand{left:192px;top:28px}
.card--back .brand__name{font-size:21px;line-height:20px}
.card--back .brand__mark{width:18px;height:18px}
.card--back .brand__tagline{font-size:6px}
.offer{position:absolute;left:39px;top:168px;width:140px;text-align:center}
.offer__free{font-family:"Oswald",sans-serif;font-weight:600;font-size:46px;line-height:48px;color:var(--orange);letter-spacing:1px}
.offer__item{font-family:"Cormorant Garamond",serif;font-style:italic;font-weight:600;font-size:17px;line-height:21px;color:var(--ink);margin-top:4px}
.slogan{position:absolute;left:345px;top:338px;font-family:"Cormorant Garamond",serif;font-style:italic;font-weight:500;font-size:31px;color:var(--paper);white-space:nowrap}
.promise{position:absolute;left:28px;top:414px;font-family:"Arimo",sans-serif;font-size:27px;line-height:32px;color:var(--grey)}
.callout{position:absolute;left:418px;top:418px;font-family:"Arimo",sans-serif;font-size:23px;color:var(--blue)}
.web-pill{position:absolute;left:417px;top:451px;width:300px;height:21px;border-radius:11px;background:var(--blue);color:var(--paper);font-family:"Arimo",sans-serif;font-size:12.5px;letter-spacing:1.6px;text-align:center;line-height:21px}
.services__label{position:absolute;left:126px;top:168px;width:154px;height:22px;font-family:"Arimo",sans-serif;font-weight:400;font-size:17px;color:var(--blue);text-align:center;line-height:22px}
.services__list{position:absolute;top:204px;list-style:none;font-size:11.8px;line-height:17.5px;color:var(--ink)}
.services__list li::before{content:"";display:inline-block;width:4px;height:4px;border-radius:50%;background:var(--orange);margin-right:5px;vertical-align:middle}
.services__list--a{left:23px}
.services__list--b{left:141px}
.payment{position:absolute;left:26px;top:285px;font-size:13px;line-height:16px;color:var(--blue)}
.about{position:absolute;left:26px;top:325px;width:276px;font-size:11.2px;line-height:13.5px;color:var(--ink);text-align:justify}
.contact{position:absolute;left:66px;top:432px;display:flex;align-items:center;gap:6px;font-family:"Arimo",sans-serif;font-weight:700;font-size:19px;color:var(--paper)}
.contact__web{position:absolute;left:57px;top:458px;font-family:"Arimo",sans-serif;font-weight:700;font-size:9.5px;letter-spacing:1.4px;color:var(--paper)}
.stamp{position:absolute;left:634px;top:25px;width:88px;height:86px;background:var(--stamp)}
</style>
</head>
<body>

<section class="card card--front">
  <svg class="card__shapes" viewBox="0 0 744 496">
    <defs>
      <linearGradient id="portraitTone" x1="0" y1="0" x2="1" y2="0">
        <stop offset="0" stop-color="#ffffff"/>
        <stop offset="0.35" stop-color="#f1d9c9"/>
        <stop offset="1" stop-color="#d9b29c"/>
      </linearGradient>
      <linearGradient id="brushTone" x1="0" y1="0" x2="1" y2="0">
        <stop offset="0" stop-color="#e6eef3"/>
        <stop offset="1" stop-color="#c8d6de"/>
      </linearGradient>
      <linearGradient id="leafTone" x1="0" y1="0" x2="1" y2="0">
        <stop offset="0" stop-color="#f37122"/>
        <stop offset="0.5" stop-color="#f6935a"/>
        <stop offset="1" stop-color="#f37122"/>
      </linearGradient>
    </defs>
    <rect x="380" y="0" width="364" height="340" fill="url(#portraitTone)" role="img" aria-label="Photo of a smiling young woman touching her cheek"/>
    <path d="M0,300 C90,318 200,332 300,330 L300,352 C200,356 90,350 0,338 Z" fill="var(--orange)"/>
    <path d="M0,342 C90,354 200,360 300,356 L300,366 C200,370 90,366 0,356 Z" fill="var(--blue)"/>
    <path d="M0,372 C100,382 210,386 300,382 L300,386 C210,390 100,388 0,377 Z" fill="var(--blue)"/>
    <path d="M290,360 C400,300 560,300 744,322 L744,350 C600,405 420,415 300,392 Z" fill="url(#leafTone)"/>
    <path d="M280,355 C420,290 600,285 744,312 L744,322 C600,298 420,302 290,362 Z" fill="var(--blue)"/>
    <path d="M300,398 C430,420 600,410 744,355 L744,385 C600,430 430,432 300,402 Z" fill="var(--blue)"/>
    <circle cx="109" cy="217" r="78" fill="var(--paper)" stroke="var(--blue)" stroke-width="6"/>
    <path d="M24,252 A92,92 0 0 1 180,160" fill="none" stroke="var(--orange)" stroke-width="9"/>
    <rect x="200" y="136" width="112" height="262" rx="18" fill="url(#brushTone)" role="img" aria-label="Electric toothbrush with travel case"/>
  </svg>

  <div class="brand">
    <span class="brand__mark"></span>
    <div>
      <div class="brand__name">Brenwick<br>DentalHub</div>
      <div class="brand__tagline">Professional Dental Services for the Charlotte Area</div>
    </div>
  </div>

  <div class="offer">
    <div class="offer__free">FREE</div>
    <div class="offer__item">Veltora Brightwave<br>toothbrush</div>
  </div>

  <p class="slogan">We love to see you smile</p>
  <p class="promise">OUR PATIENTS ARE OUR<br>MOST IMPORTANT ASSET</p>
  <p class="callout">CALL US: (704) 555-0186</p>
  <p class="web-pill">www.brenwickdentalhub.com</p>
</section>

<section class="card card--back">
  <svg class="card__shapes" viewBox="0 0 744 496">
    <defs>
      <linearGradient id="backdropTone" x1="0" y1="0" x2="1" y2="1">
        <stop offset="0" stop-color="#d8c2b4"/>
        <stop offset="0.4" stop-color="#e9eef1"/>
        <stop offset="1" stop-color="#f4f6f7"/>
      </linearGradient>
      <linearGradient id="ribbonTone" x1="0" y1="0" x2="1" y2="0">
        <stop offset="0" stop-color="#f37122"/>
        <stop offset="0.5" stop-color="#fbc9a6"/>
        <stop offset="1" stop-color="#f37122"/>
      </linearGradient>
    </defs>
    <path d="M0,0 H372 C392,60 390,120 372,150 C260,140 120,165 0,205 Z" fill="url(#backdropTone)" role="img" aria-label="Photo of a smiling woman in a knit hat looking up thoughtfully"/>
    <path d="M0,205 C120,165 260,140 372,150 L372,158 C260,150 120,175 0,214 Z" fill="var(--blue)"/>
    <path d="M345,0 H362 C430,110 430,270 370,350 C300,420 160,420 0,398 L0,392 C160,410 290,405 355,342 C410,262 412,110 345,0 Z" fill="var(--orange)"/>
    <path d="M0,412 C150,428 300,420 362,360 C420,300 440,180 418,40 C450,170 445,330 385,496 L0,496 Z" fill="var(--blue)"/>
    <path d="M126,168 L280,168 L271,179 L280,190 L126,190 L135,179 Z" fill="url(#ribbonTone)"/>
  </svg>

  <div class="brand">
    <span class="brand__mark"></span>
    <div>
      <div class="brand__name">Brenwick<br>DentalHub</div>
      <div class="brand__tagline">Professional Dental Services for the Charlotte Area</div>
    </div>
  </div>

  <h2 class="services__label">SERVICES:</h2>
  <ul class="services__list services__list--a">
    <li>LUMAX crowns</li>
    <li>Cosmetic veneers</li>
    <li>Whitening</li>
    <li>Root canals</li>
  </ul>
  <ul class="services__list services__list--b">
    <li>Tooth-colored composite (fillings)</li>
    <li>Clear orthodontic treatments (alignira)</li>
    <li>LUMAX onlay/inlays</li>
    <li>Dentures</li>
  </ul>

  <p class="payment">we have flexible payment options with PayBloom,<br>and that we work with most insurance plans</p>
  <p class="about">Brenwick DentalHub offers the latest invisible braces, advanced teeth whitening techniques as well as preventative and restorative procedures for patients of all ages.</p>

  <p class="contact">
    <svg width="20" height="20" viewBox="0 0 20 20" aria-hidden="true"><circle cx="10" cy="10" r="8.5" fill="none" stroke="#fff" stroke-width="1.6"/><path d="M7,5.5 L8.6,5.5 L9.3,8 L8.2,8.9 C8.8,10.2 9.8,11.2 11.1,11.8 L12,10.7 L14.5,11.4 L14.5,13 C11,13.5 6.5,9 7,5.5 Z" fill="#fff"/></svg>
    (704) 555-0186
  </p>
  <p class="contact__web">www.brenwickdentalhub.com</p>

  <div class="stamp"></div>
</section>

</body>
</html>
```